Business Card for Wellness Clinic

We need a business card for our new logo. I want it to match the feel of the logo

Target Market(s)

Young professional families looking for holistic health care

Industry/Entity Type

Health And Wellness

Contact Information for Business Card

Our business Name: Brackenfield Health & wellness Centre, our phone #, email address...see attached old business card

Font styles to use
Sans Serif

Colors
33b8a4
cee9f5

Requirements
Must have
• my logo and business name
• Font is "Helvetica Neue LT Std 45 Light" and
• Only for "&" using font "Trajan pro bold"
• Use colors in the logo

```html
<!DOCTYPE html>
<html lang="en">
<head>
<meta charset="utf-8">
<title>Brackenfield Health &amp; wellness Centre – Business Card</title>
<link href="https://fonts.googleapis.com/css2?family=Roboto:wght@300;400&display=swap" rel="stylesheet">
<style>
  :root {
    --teal: #3cc2a5;
    --band-shadow: #cfd3d2;
    --grey: #9a9c9c;
    --card: #ffffff;
    --backdrop: #e9ecec;
  }
  * { box-sizing: border-box; margin: 0; padding: 0; }
  html, body { width: 1200px; height: 900px; overflow: hidden; }
  body {
    background: var(--backdrop);
    font-family: "Roboto", "Helvetica Neue", Arial, sans-serif;
    font-weight: 300;
    position: relative;
  }
  .card {
    position: absolute;
    left: 285px;
    width: 630px;
    height: 360px;
    background: var(--card);
    box-shadow: 0 6px 18px rgba(0,0,0,0.12);
  }
  .card--front { top: 70px; }
  .card--back { top: 470px; }

  .brand {
    position: absolute;
    top: 34px;
    left: 0;
    right: 0;
    display: flex;
    align-items: center;
    justify-content: center;
    gap: 16px;
  }
  .brand__mark { width: 34px; height: 34px; background: var(--teal); flex: none; }
  .brand__name {
    color: var(--grey);
    font-weight: 300;
    text-transform: uppercase;
    white-space: nowrap;
    line-height: 1.15;
  }
  .brand__line { display: block; font-size: 24px; letter-spacing: 4px; }
  .brand__line--sub { font-size: 15px; letter-spacing: 9px; margin-top: 4px; }

  .card--back .brand { justify-content: flex-start; left: 46px; top: 30px; }
  .card--back .brand__line { font-size: 21px; }
  .card--back .brand__line--sub { font-size: 13px; letter-spacing: 8px; }

  .practitioner { position: absolute; top: 128px; left: 0; right: 0; text-align: center; }
  .practitioner__name { color: var(--teal); font-size: 28px; font-weight: 300; white-space: nowrap; }
  .practitioner__title { color: var(--grey); font-size: 15px; margin-top: 4px; }

  .contact-band {
    position: absolute;
    left: 22px; right: 22px; bottom: 26px;
    height: 80px;
    background: var(--teal);
    box-shadow: 0 8px 0 var(--band-shadow);
    display: flex;
    align-items: center;
    justify-content: space-between;
    padding: 0 16px;
    color: #fff;
    font-size: 12px;
    line-height: 1.4;
  }
  .contact { display: flex; align-items: center; gap: 8px; }
  .contact p { white-space: nowrap; }
  .contact svg { width: 20px; height: 20px; flex: none; }

  .appointment {
    position: absolute;
    left: 22px; right: 22px; bottom: 26px;
    height: 200px;
    background: var(--teal);
    box-shadow: 0 8px 0 var(--band-shadow);
    padding: 22px 26px;
  }
  .appointment__form {
    background: #fff;
    padding: 14px 18px;
    color: var(--grey);
    font-size: 16px;
    line-height: 2;
  }
  .field-row { display: flex; gap: 16px; }
  .field { display: flex; flex: 1; align-items: baseline; gap: 6px; }
  .field__line { flex: 1; border-bottom: 1px solid var(--grey); height: 1em; }
  .appointment__note {
    color: #fff;
    font-size: 15px;
    line-height: 1.4;
    margin-top: 16px;
    white-space: nowrap;
  }
</style>
</head>
<body>

<section class="card card--front" aria-label="Business card front">
  <div class="brand">
    <span class="brand__mark"></span>
    <span class="brand__name">
      <span class="brand__line">Brackenfield Health</span>
      <span class="brand__line brand__line--sub">&amp; wellness Centre</span>
    </span>
  </div>
  <div class="practitioner">
    <p class="practitioner__name">Dr. Elena Marsh, N.D.</p>
    <p class="practitioner__title">Naturopathic Doctor</p>
  </div>
  <div class="contact-band">
    <div class="contact">
      <svg viewBox="0 0 24 24" aria-hidden="true"><path d="M12 3 2 12h3v9h5v-6h4v6h5v-9h3z" fill="#fff"/></svg>
      <p>48 Larkspur Ave. E, Suite 310<br>Ottawa, ON K1R 2M7</p>
    </div>
    <div class="contact">
      <svg viewBox="0 0 24 24" aria-hidden="true"><path d="M6.6 10.8a15 15 0 0 0 6.6 6.6l2.2-2.2c.3-.3.7-.4 1-.2 1.1.4 2.3.6 3.6.6.6 0 1 .4 1 1V20c0 .6-.4 1-1 1A17 17 0 0 1 3 4c0-.6.4-1 1-1h3.5c.6 0 1 .4 1 1 0 1.3.2 2.5.6 3.6.1.3 0 .7-.2 1z" fill="#fff"/></svg>
      <p>T: 613-555-0148<br>F: 888-555-0172</p>
    </div>
    <div class="contact">
      <svg viewBox="0 0 24 24" aria-hidden="true" fill="none" stroke="#fff" stroke-width="1.6"><circle cx="12" cy="12" r="9"/><ellipse cx="12" cy="12" rx="4" ry="9"/><path d="M3 12h18M5 7h14M5 17h14"/></svg>
      <p>emarsh@brackenfieldwellness.ca<br>www.brackenfieldwellness.ca</p>
    </div>
  </div>
</section>

<section class="card card--back" aria-label="Business card back">
  <div class="brand">
    <span class="brand__mark"></span>
    <span class="brand__name">
      <span class="brand__line">Brackenfield Health</span>
      <span class="brand__line brand__line--sub">&amp; wellness Centre</span>
    </span>
  </div>
  <div class="appointment">
    <div class="appointment__form">
      <div class="field-row">
        <div class="field">Date:<span class="field__line"></span></div>
        <div class="field">Time:<span class="field__line"></span></div>
      </div>
      <div class="field">For:<span class="field__line"></span></div>
    </div>
    <p class="appointment__note">If you are unable to keep your appointment. Please provide<br>at least 2 business day notice or full visit fees will apply.</p>
  </div>
</section>

</body>
</html>
```